Austrian finance und insurance broker needs business card design

We Need a serious looking Design for Business Card. we consult private and corporates customers in finance and insurance questions. the final design should express security and experience. We consult customers in questions of loans, Investments and insurance and have a wide range of Banks to offer. We compare several offers and select the best for our customers.

Target Market(s)

private and coporate customers with efforts in Money and insurance

Industry/Entity Type

Insurance Broker

Contact Information for Business Card

Bernhard Aigner
Geschäftsführer
staatl. geprüfter Vermögensberater und Versicherungsmakler
Tel: 0664 521 8409
office@der-brandl.at
www.der-brandl.at
Leopold Hainz Gasse 14
2183 Melkstetten
GISA Nr. 48270315 u. 51736048 (backside)

Font styles to use
Serif
Sans Serif

Requirements
Must have
• logo (designcrowd zip) and all Details
Nice to have
• makler logo design, maybe a 2 coloured Version is possible

```html
<!DOCTYPE html>
<html lang="de">
<head>
<meta charset="utf-8">
<title>Aigner Vermögensberatung – Visitenkarte</title>
<link rel="stylesheet" href="https://fonts.googleapis.com/css2?family=Open+Sans:wght@400;600;700&family=Quicksand:wght@700&display=swap">
<style>
  :root {
    --stage: #e9e7e3;
    --paper: #fbfbfb;
    --ink-grey: #6b6b6b;
    --ink-dark: #4a4a4a;
    --brand-blue: #2e5fb4;
    --band-blue: #2d62bf;
    --slate: #2b2c31;
    --slate-ring: #35363b;
    --badge-red: #b8163a;
    --white: #ffffff;
  }
  * { box-sizing: border-box; margin: 0; padding: 0; }
  html, body { width: 1200px; height: 942px; overflow: hidden; }
  body {
    background: var(--stage);
    font-family: "Open Sans", Arial, sans-serif;
    position: relative;
  }
  .card {
    position: absolute;
    left: 275px;
    width: 650px;
    height: 420px;
    border-radius: 4px;
    box-shadow: 0 8px 24px rgba(0,0,0,.18);
    overflow: hidden;
  }
  .card--front { top: 30px; background: var(--paper); }
  .card--back { top: 492px; background: var(--slate); }

  /* brand lockup */
  .lockup { position: absolute; display: flex; align-items: center; }
  .lockup__mark {
    border-radius: 50%;
    border: 4px solid var(--brand-blue);
    flex: none;
  }
  .lockup__rule { width: 2px; align-self: stretch; margin: 0 14px; }
  .lockup__name {
    font-family: "Quicksand", "Open Sans", sans-serif;
    font-weight: 700;
    color: var(--brand-blue);
    line-height: 1.15;
  }
  .lockup__tagline { font-family: "Open Sans", sans-serif; font-weight: 400; }

  .card--front .lockup { left: 34px; top: 30px; }
  .card--front .lockup__mark { width: 66px; height: 66px; }
  .card--front .lockup__rule { background: var(--ink-dark); height: 62px; align-self: center; width: 1.5px; }
  .card--front .lockup__name { font-size: 17px; }
  .card--front .lockup__tagline { font-size: 11.5px; color: var(--ink-dark); margin-top: 2px; }

  .person {
    position: absolute; left: 34px; top: 128px;
  }
  .person__name {
    font-size: 30px; font-weight: 700; letter-spacing: 1px;
    color: var(--ink-grey); text-transform: uppercase;
  }
  .person__rule {
    position: absolute; left: 346px; right: 0; top: 160px;
    height: 2px; background: var(--brand-blue);
  }
  .person__role { font-size: 15.5px; color: var(--brand-blue); margin-top: 8px; line-height: 1.35; }

  .contact { position: absolute; font-size: 17px; color: var(--ink-grey); }
  .contact li { list-style: none; display: flex; align-items: center; gap: 12px; margin-bottom: 8px; }
  .contact svg { width: 16px; height: 16px; flex: none; fill: var(--brand-blue); }
  .contact--left { left: 34px; top: 262px; }
  .contact--right { right: 40px; top: 300px; }
  .contact--right li { flex-direction: row-reverse; }
  .contact__divider {
    position: absolute; left: 300px; top: 318px; width: 1.5px; height: 52px; background: var(--brand-blue);
  }
  .partner-badge {
    position: absolute; right: 40px; top: 200px; width: 74px; height: 74px;
    border-radius: 50%; background: var(--badge-red);
  }

  /* back */
  .back__ring {
    position: absolute; left: 330px; top: 40px; width: 290px; height: 290px;
    border-radius: 50%; border: 14px solid var(--slate-ring);
  }
  .card--back .lockup { left: 120px; top: 70px; }
  .card--back .lockup__mark { width: 120px; height: 120px; }
  .card--back .lockup__rule { background: var(--white); height: 110px; align-self: center; width: 2.5px; transform: skewX(-20deg); margin: 0 22px; }
  .card--back .lockup__name { font-size: 26px; }
  .card--back .lockup__tagline { font-size: 20px; color: var(--white); font-weight: 600; margin-top: 6px; }
  .gisa-band {
    position: absolute; left: 70px; bottom: 0; width: 420px; height: 92px;
    background: var(--band-blue);
    clip-path: polygon(0 0, 92% 0, 100% 100%, 0 100%);
    display: flex; align-items: center; padding-left: 40px;
    color: var(--white); font-size: 21px; letter-spacing: .5px;
  }
</style>
</head>
<body>

<section class="card card--front" aria-label="Visitenkarte Vorderseite">
  <div class="lockup">
    <div class="lockup__mark"></div>
    <div class="lockup__rule"></div>
    <div>
      <div class="lockup__name">Aigner Vermögensberatung GmbH</div>
      <div class="lockup__tagline">Finanzieren, Versichern, Vorsorgen</div>
    </div>
  </div>

  <div class="person">
    <h1 class="person__name">Bernhard Aigner</h1>
    <p class="person__role">Geschäftsführer<br>staatl. geprüfter Vermögensberater und Versicherungsmakler</p>
  </div>
  <div class="person__rule"></div>

  <div class="partner-badge" role="img" aria-label="Partnerabzeichen Versicherungsmakler"></div>

  <ul class="contact contact--left">
    <li>
      <svg viewBox="0 0 24 24"><path d="M6.6 10.8a15 15 0 0 0 6.6 6.6l2.2-2.2a1 1 0 0 1 1-.25 11.4 11.4 0 0 0 3.6.57 1 1 0 0 1 1 1V20a1 1 0 0 1-1 1A17 17 0 0 1 3 4a1 1 0 0 1 1-1h3.5a1 1 0 0 1 1 1c0 1.25.2 2.45.57 3.57a1 1 0 0 1-.25 1z"/></svg>
      0664 521 8409
    </li>
    <li>
      <svg viewBox="0 0 24 24"><path d="M12 2a7 7 0 0 0-7 7c0 5.25 7 13 7 13s7-7.75 7-13a7 7 0 0 0-7-7zm0 9.5A2.5 2.5 0 1 1 12 6.5a2.5 2.5 0 0 1 0 5z"/></svg>
      Leopold Hainz Gasse 14, 2183 Melkstetten
    </li>
  </ul>

  <div class="contact__divider"></div>

  <ul class="contact contact--right">
    <li>
      <svg viewBox="0 0 24 24"><path d="M2 5h20v14H2zm2 2v.5l8 5 8-5V7l-8 5z"/></svg>
      office@der-brandl.at
    </li>
    <li>
      <svg viewBox="0 0 24 24" fill="none"><circle cx="12" cy="12" r="9" fill="none" stroke="#2e5fb4" stroke-width="1.6"/><path d="M3 12h18M12 3c3 3.5 3 14.5 0 18M12 3c-3 3.5-3 14.5 0 18" fill="none" stroke="#2e5fb4" stroke-width="1.4"/></svg>
      www.der-brandl.at
    </li>
  </ul>
</section>

<section class="card card--back" aria-label="Visitenkarte Rückseite">
  <div class="back__ring"></div>
  <div class="lockup">
    <div class="lockup__mark"></div>
    <div class="lockup__rule"></div>
    <div>
      <div class="lockup__name">Aigner Vermögensberatung GmbH</div>
      <div class="lockup__tagline">Finanzieren, Versichern, Vorsorgen</div>
    </div>
  </div>
  <div class="gisa-band">GISA Nr. 48270315 u. 51736048</div>
</section>

</body>
</html>
```